Brook Forge - Crypto Currency Miner Powered by Renewable Energy Website

We Need Web Pages Design for Website for Crypto Currency Miner

Serivices include:
Mining Rig Sales
Housing for Rigs turnkey on renewable energy grid
Cloud Mining term packages
Updates

http://www.vaultrigdigest.example (Competitors sites)

Target Market(s)

Investers for Mining Rigs and terms for 1,2 or 3 years of Hash rate

Industry/Entity Type

Mining

Number of Pages Required

5+ page

Font styles to use
Sans Serif

Colors
add136
9bcb3c
606060
474747
ffc214
cadf82
fbee3e
876aae
6b449b

Requirements
Must have
• Pictures of Solar, Wind and power Factor Correction units
Nice to have
• e-commerce platform so contract terms can be purchased through website
Should not have
• Heavy construction equipment

```html
<!DOCTYPE html>
<html lang="en">
<head>
<meta charset="utf-8">
<title>Brook Forge – Crypto Currency Miner</title>
<link href="https://fonts.googleapis.com/css2?family=Oswald:wght@400;500;600&family=PT+Sans:wght@400;700&display=swap" rel="stylesheet">
<style>
:root{
  --yellow:#ffc214;
  --green:#add136;
  --green-deep:#3aa646;
  --purple:#6b449b;
  --purple-soft:#876aae;
  --ink:#222222;
  --grey:#606060;
  --grey-dark:#474747;
  --footer:#2c2c2c;
  --footer-box:#3a3a3a;
  --white:#ffffff;
}
*{box-sizing:border-box;margin:0;padding:0}
html,body{width:1200px;height:2761px;overflow:hidden}
body{position:relative;font-family:"PT Sans",Arial,sans-serif;color:var(--ink);background:var(--white)}
.abs{position:absolute}
.head{font-family:"Oswald",Arial,sans-serif}
.btn{position:absolute;display:flex;align-items:center;justify-content:center;font-family:"Oswald",Arial,sans-serif;font-size:15px;color:var(--white);background:var(--yellow)}

/* top bar */
.topbar{left:0;top:0;width:1200px;height:46px;background:var(--white)}
.social-label{left:200px;top:14px;font-size:13px;color:var(--grey-dark)}
.social-dots{left:280px;top:16px;display:flex;gap:20px}
.social-dots span{width:12px;height:12px;border-radius:50%;background:#b8b8b8;display:block}
.signin{left:858px;top:14px;font-size:13px;color:var(--grey-dark)}
.register{left:912px;top:0;width:90px;height:46px;font-size:12px}

/* hero */
.hero{left:0;top:46px;width:1200px;height:617px;background:linear-gradient(180deg,#4a5a70 0%,#7a8aa0 35%,#3c4a5c 55%,#2f4a2a 80%,#27401f 100%)}
.brand{left:200px;top:92px;display:flex;align-items:center;gap:10px}
.brand-dot{width:34px;height:34px;border-radius:50%;background:var(--green-deep)}
.brand-name{font-family:"PT Sans",Arial,sans-serif;font-weight:700;font-size:26px;color:var(--white)}
.contacts{left:510px;top:92px;display:flex;gap:26px;align-items:center}
.contact{display:flex;align-items:center;gap:10px;font-size:13px;color:var(--white)}
.contact .ring{width:36px;height:36px;border-radius:50%;border:1px solid rgba(255,255,255,.7);display:flex;align-items:center;justify-content:center}
.nav{left:200px;top:182px;width:801px;height:41px;background:var(--yellow);display:flex;align-items:center;padding-left:26px}
.nav a{font-family:"Oswald",Arial,sans-serif;font-size:15px;color:var(--white);text-decoration:none;margin-right:42px}
.nav .search{position:absolute;right:16px;top:12px}
.hero-title{left:200px;top:322px;font-size:50px;font-weight:500;color:var(--white)}
.hero-title em{font-style:normal;color:var(--yellow)}
.hero-text{left:200px;top:402px;width:470px;font-size:14px;line-height:22px;color:var(--white)}
.get-started{left:200px;top:497px;width:147px;height:44px}
.read-more-outline{left:360px;top:497px;width:148px;height:44px;background:transparent;border:1px solid var(--white)}
.dots{left:582px;top:594px;display:flex;gap:5px}
.dots span{width:9px;height:9px;border-radius:50%;background:var(--white)}
.dots span:first-child{background:var(--yellow)}

/* about */
.about{left:0;top:663px;width:1200px;height:419px;background:linear-gradient(135deg,#f4f4f4,#e6e6e6 60%,#f2f2f2)}
.about-title{left:200px;top:730px;font-size:30px;font-weight:500}
.about-lead{left:200px;top:786px;width:360px;font-size:19px;line-height:28px}
.about-text{left:200px;top:848px;width:360px;font-size:12px;line-height:22px;color:var(--grey-dark)}
.about-btn{left:200px;top:965px;width:110px;height:42px;font-size:13px}
.laptop{left:558px;top:745px;width:502px;height:276px}
.laptop-screen{position:absolute;left:62px;top:0;width:378px;height:246px;background:#1e1e1e;border-radius:10px;padding:12px}
.laptop-display{width:100%;height:100%;background:linear-gradient(135deg,#45b74a,#2e9f3a);display:flex;align-items:center;justify-content:center;gap:10px}
.laptop-display .mark-dot{width:40px;height:40px;border-radius:50%;background:var(--white)}
.laptop-display .mark-name{font-weight:700;font-size:32px;color:var(--white)}
.laptop-base{position:absolute;left:0;top:246px;width:502px;height:18px;background:linear-gradient(#e2e2e2,#9a9a9a);border-radius:0 0 40px 40px}

/* services */
.services-title{left:0;top:1148px;width:1200px;text-align:center;font-size:30px;font-weight:500}
.rule{position:absolute;height:2px;background:var(--grey-dark)}
.service{position:absolute;top:1237px;width:284px;height:211px;text-align:center}
.service.is-featured{background:var(--white);box-shadow:0 2px 14px rgba(0,0,0,.15)}
.service svg{margin-top:22px}
.service h3{font-family:"Oswald",Arial,sans-serif;font-weight:500;font-size:13px;margin-top:18px;color:var(--ink)}
.service p{font-size:12px;line-height:18px;color:#8a8a8a;margin:8px auto 0;width:200px}

/* call to action */
.cta{left:0;top:1518px;width:1200px;height:469px;background:linear-gradient(180deg,#2c3340,#3a4558 45%,#232a36)}
.phone{left:200px;top:1573px;width:269px;height:414px;background:var(--white);border-radius:40px 40px 0 0}
.phone-cam{position:absolute;left:129px;top:20px;width:10px;height:10px;border-radius:50%;background:#333}
.phone-screen{position:absolute;left:16px;top:66px;width:237px;height:348px;background:linear-gradient(160deg,#52c05a,#2a9a36);border:2px solid #222;display:flex;align-items:center;justify-content:center;gap:8px}
.phone-screen .mark-dot{width:30px;height:30px;border-radius:50%;background:var(--white)}
.phone-screen .mark-name{font-weight:700;font-size:26px;color:var(--white)}
.cta-title{left:584px;top:1640px;width:400px;text-align:center;font-size:30px;line-height:40px;font-weight:500;color:var(--yellow)}
.cta-text{left:614px;top:1770px;width:340px;text-align:center;font-size:12px;line-height:21px;color:var(--white)}
.cta-btn{left:738px;top:1877px;width:110px;height:42px;font-size:13px}

/* contract terms */
.contract-title{left:170px;top:2062px;width:400px;text-align:center;font-size:30px;font-weight:500}
.contract-text{left:200px;top:2133px;width:342px;text-align:center;font-size:12px;line-height:21px;color:var(--grey-dark)}
.contract-btn{left:278px;top:2239px;width:188px;height:43px;font-size:13px}
.term{position:absolute;width:130px;text-align:center}
.term .diamond{width:90px;height:90px;margin:0 auto;background:var(--yellow);transform:rotate(45deg);border-radius:12px;display:flex;align-items:center;justify-content:center}
.term .diamond svg{transform:rotate(-45deg)}
.term span{display:block;margin-top:28px;font-family:"Oswald",Arial,sans-serif;font-size:16px;color:var(--ink)}

/* footer */
.footer{left:0;top:2407px;width:1200px;height:354px;background:var(--footer)}
.footer-brand{left:200px;top:2389px;width:258px;height:205px;background:var(--footer-box);padding:20px}
.footer-brand h4{font-family:"Oswald",Arial,sans-serif;font-weight:400;font-size:28px;color:var(--yellow)}
.footer-brand p{font-size:12px;line-height:20px;color:var(--white);margin-top:14px}
.footer-brand .more{display:block;margin-top:14px;font-size:12px;font-weight:700;color:var(--yellow)}
.footer-social{left:200px;top:2612px;display:flex;gap:10px}
.footer-social span{width:38px;height:38px;border-radius:50%;background:var(--white);display:block}
.col-title{font-family:"Oswald",Arial,sans-serif;font-size:14px;color:var(--yellow)}
.links{list-style:none;font-size:12px;color:var(--white)}
.links li{height:26px;display:flex;align-items:center;gap:10px}
.links li::before{content:"";border-left:6px solid var(--white);border-top:4px solid transparent;border-bottom:4px solid transparent}
.info{list-style:none;font-size:12px;color:var(--white)}
.info li{display:flex;gap:14px;align-items:flex-start;line-height:19px;margin-bottom:12px}
.footer-line{left:0;top:2672px;width:1200px;height:1px;background:#555}
.footer-nav{left:0;top:2692px;width:1200px;display:flex;justify-content:center;gap:22px;font-size:12px;color:var(--white)}
.copyright{left:0;top:2724px;width:1200px;text-align:center;font-size:12px;color:var(--white)}
</style>
</head>
<body>

<header class="abs topbar"></header>
<div class="abs social-label">Social Links :</div>
<div class="abs social-dots"><span></span><span></span><span></span><span></span></div>
<div class="abs signin">Sign In</div>
<div class="btn register">REGISTER</div>

<section class="abs hero" role="img" aria-label="Photo of rows of solar panels on green grass with wind turbines under a cloudy sky"></section>
<div class="abs brand"><span class="brand-dot"></span><span class="brand-name">Brook Forge</span></div>
<div class="abs contacts">
  <div class="contact"><span class="ring"><svg width="14" height="14" viewBox="0 0 24 24"><path d="M6 2l4 4-2 3c1 3 4 6 7 7l3-2 4 4-3 4C10 22 2 14 2 5z" fill="#fff"/></svg></span>+1 555 014 2290</div>
  <div class="contact"><span class="ring"><svg width="14" height="14" viewBox="0 0 24 24"><path d="M3 11L12 3l9 8v10H3z" fill="none" stroke="#fff" stroke-width="2"/></svg></span>www.brookforge.example</div>
  <div class="contact"><span class="ring"><svg width="12" height="16" viewBox="0 0 24 32"><path d="M12 0C5 0 0 5 0 12c0 8 12 20 12 20s12-12 12-20C24 5 19 0 12 0z" fill="#fff"/><circle cx="12" cy="12" r="4" fill="#5a6a80"/></svg></span>Lorem ipsum is text</div>
</div>
<nav class="abs nav">
  <svg width="14" height="14" viewBox="0 0 24 24" style="margin-right:10px"><path d="M2 12L12 3l10 9h-3v9h-5v-6h-4v6H5v-9z" fill="#fff"/></svg>
  <a>Home</a><a>About Us</a><a>Services</a><a>Contract Terms</a><a>FAQ</a><a>Contact Us</a>
  <svg class="search" width="16" height="16" viewBox="0 0 24 24"><circle cx="10" cy="10" r="7" fill="none" stroke="#fff" stroke-width="3"/><path d="M15 15l7 7" stroke="#fff" stroke-width="3"/></svg>
</nav>
<h1 class="abs head hero-title"><em>Welcome</em> To Crypto Currency Miner</h1>
<p class="abs hero-text">Lorem Ipsum is simply dummy text of the printing and typesetting industry. Lorem Ipsum has been the industry's ..</p>
<div class="btn get-started">Get Started</div>
<div class="btn read-more-outline">Read More</div>
<div class="abs dots"><span></span><span></span><span></span></div>

<section class="abs about"></section>
<h2 class="abs head about-title">ABOUT US</h2>
<p class="abs about-lead">Lorem Ipsum is simply dummy text of the printing &amp; Industry..</p>
<p class="abs about-text">Lorem Ipsum is simply dummy text of the printing and typesetting industry. Lorem Ipsum has been the industry's standard dummy text ever since the 1500s, when an unknown printer took a galley of type and scrambled it to make a type specimen book.</p>
<div class="btn about-btn">Read More</div>
<div class="abs laptop">
  <div class="laptop-screen"><div class="laptop-display" role="img" aria-label="Green circuit-board screen showing the company name"><span class="mark-dot"></span><span class="mark-name">Brook Forge</span></div></div>
  <div class="laptop-base"></div>
</div>

<h2 class="abs head services-title">OUR SERVICES</h2>
<div class="rule" style="left:580px;top:1212px;width:40px"></div>
<div class="rule" style="left:590px;top:1218px;width:20px;height:1px"></div>
<div class="service" style="left:163px">
  <svg width="60" height="60" viewBox="0 0 60 60" fill="none" stroke="#6b449b" stroke-width="3"><path d="M6 18Q30 2 54 18"/><path d="M30 10v34"/><path d="M24 44h12v8H24z"/><path d="M22 30l-8 10M38 30l8 10"/></svg>
  <h3>Mining Rig Sales</h3>
  <p>Lorem Ipsum is simply dummy text of the printing and typesetting industry.</p>
</div>
<div class="service is-featured" style="left:458px">
  <svg width="60" height="60" viewBox="0 0 60 60" fill="none" stroke="#6b449b" stroke-width="3"><path d="M30 4v8"/><path d="M22 16h16M18 30h24M12 54h36"/><path d="M24 16l-6 38M36 16l6 38"/><path d="M22 30l14 24M38 30L24 54"/></svg>
  <h3>Housing for Rigs turnkey on renewable energy grid</h3>
  <p>Lorem Ipsum is simply dummy text of the printing and typesetting industry.</p>
</div>
<div class="service" style="left:752px">
  <svg width="64" height="60" viewBox="0 0 64 60" fill="none" stroke="#6b449b" stroke-width="3"><path d="M16 46H12a10 10 0 010-20 16 16 0 0131-6 12 12 0 0110 26h-5"/><ellipse cx="32" cy="38" rx="10" ry="4"/><path d="M22 38v12c0 2 4 4 10 4s10-2 10-4V38M22 44c0 2 4 4 10 4s10-2 10-4"/></svg>
  <h3>Cloud Mining term packages</h3>
  <p>Lorem Ipsum is simply dummy text of the printing and typesetting industry.</p>
</div>

<section class="abs cta" role="img" aria-label="Dark photo of solar panels under an evening sky"></section>
<div class="abs phone">
  <span class="phone-cam"></span>
  <div class="phone-screen" role="img" aria-label="Green circuit-board app screen showing the company name"><span class="mark-dot"></span><span class="mark-name">Brook Forge</span></div>
</div>
<h2 class="abs head cta-title">TRY CRYPTO CURRENCY MINER TODAY</h2>
<div class="rule" style="left:764px;top:1743px;width:40px;background:#fff"></div>
<div class="rule" style="left:774px;top:1749px;width:20px;height:1px;background:#fff"></div>
<p class="abs cta-text">Lorem Ipsum is simply dummy text of the printing and typesetting industry. Lorem Ipsum has been the industry's standard dummy text ever since the 1500s, when an unknown printer took galley of type and scrambled specimen book.</p>
<div class="btn cta-btn">Contact Us</div>

<h2 class="abs head contract-title">PURCHASE CONTRACT TERMS</h2>
<p class="abs contract-text">Lorem Ipsum is simply dummy text of the printing and typesetting industry. Lorem Ipsum has been the industry's standard dummy text ever since the 1500s, when an unknown printer took galley of type and scrambled specimen book.</p>
<div class="btn contract-btn">Please Login to Purchase</div>
<div class="term" style="left:612px;top:2174px">
  <div class="diamond"><svg width="40" height="40" viewBox="0 0 40 40" fill="none" stroke="#222" stroke-width="2"><rect x="6" y="12" width="28" height="20" rx="2"/><circle cx="20" cy="8" r="5"/><path d="M12 20h6M12 26h10"/></svg></div>
  <span>1 Years</span>
</div>
<div class="term" style="left:741px;top:2086px">
  <div class="diamond"><svg width="40" height="40" viewBox="0 0 40 40" fill="none" stroke="#222" stroke-width="2"><rect x="6" y="12" width="28" height="20" rx="2"/><circle cx="20" cy="8" r="5"/><path d="M12 20h6M12 26h10"/></svg></div>
  <span>2 Years</span>
</div>
<div class="term" style="left:870px;top:2174px">
  <div class="diamond"><svg width="40" height="40" viewBox="0 0 40 40" fill="none" stroke="#222" stroke-width="2"><rect x="6" y="12" width="28" height="20" rx="2"/><circle cx="20" cy="8" r="5"/><path d="M12 20h6M12 26h10"/></svg></div>
  <span>3 Years</span>
</div>

<footer class="abs footer" role="img" aria-label="Dark street map background"></footer>
<div class="abs footer-brand">
  <h4>The Brook Forge</h4>
  <p>Lorem Ipsum is simply dummy text of tprinting and typesetting industry. Lor Ipsuhas been the industry's..</p>
  <span class="more">→ READ MORE</span>
</div>
<div class="abs footer-social"><span></span><span></span><span></span><span></span></div>
<div class="abs col-title" style="left:477px;top:2452px">QUICK LINK</div>
<ul class="abs links" style="left:477px;top:2474px"><li>About Us</li><li>Support Center</li><li>Terms of Use</li><li>Login</li><li>Account</li><li>Contact</li></ul>
<ul class="abs links" style="left:642px;top:2474px"><li>User Feedback</li><li>Privacy Policy</li><li>Help</li></ul>
<div class="abs col-title" style="left:804px;top:2452px">CONTACT INFORMATION</div>
<ul class="abs info" style="left:804px;top:2483px;width:200px">
  <li><svg width="14" height="14" viewBox="0 0 24 24"><path d="M6 2l4 4-2 3c1 3 4 6 7 7l3-2 4 4-3 4C10 22 2 14 2 5z" fill="#fff"/></svg>+1 555 014 2290</li>
  <li><svg width="14" height="18" viewBox="0 0 24 32"><path d="M12 0C5 0 0 5 0 12c0 8 12 20 12 20s12-12 12-20C24 5 19 0 12 0z" fill="#fff"/></svg>Lorem Ipsum is simply dummy of the printing</li>
  <li><svg width="14" height="12" viewBox="0 0 24 18"><rect x="1" y="1" width="22" height="16" fill="none" stroke="#fff" stroke-width="2"/><path d="M1 1l11 9 11-9" fill="none" stroke="#fff" stroke-width="2"/></svg>info@brookforge.example</li>
  <li><svg width="14" height="14" viewBox="0 0 24 24" fill="none" stroke="#fff" stroke-width="2.5"><path d="M10 14l4-4M8 12l-3 3a3 3 0 004 4l3-3M16 12l3-3a3 3 0 00-4-4l-3 3"/></svg>https://www.brookforge.example</li>
</ul>
<div class="abs footer-line"></div>
<div class="abs footer-nav"><span>Home</span><span>|</span><span>About Us</span><span>|</span><span>Services</span><span>|</span><span>Contract Terms</span><span>|</span><span>FAQ</span><span>|</span><span>Contact Us</span></div>
<div class="abs copyright">© Copyright 2018 the brook forge. All Rights Reserved.</div>

</body>
</html>
```